Corvella Foundation is a new grant making charity set up in the UK.

Having got a logo, we now need a website to go with it. We have worked out the text which people are going to need in order to then apply for grants. But having found out what we require they will probably need to go away and think about it.
We have to be careful of what images we use. So I have uploaded some images that we like. We are also going to be adding more pages almost immediately so need to think about the images for these.
I know basic wordpress so I will be able to add new pages/make alterations in future.
Updates
The website does need to be coded in Wordpress so that I can maintain it afterwards.
Marisse
Brief changed to provide more money and we have also provided more possible pictures. And generally more explanation.
Target Market(s)
departments in universities, other charities doing work on relief of pain, people working in health service departments
Industry/Entity Type
Health Charity
Coding
Coded - Design and coding required
Number of Pages Required
4 page
Look and feel
Each slider illustrates characteristics of the customer's brand and the style your logo design should communicate.

```html
<!DOCTYPE html>
<html lang="en">
<head>
<meta charset="utf-8">
<title>Corvella Foundation</title>
<link rel="stylesheet" href="https://fonts.googleapis.com/css2?family=Montserrat:wght@400;600;700;800&family=Roboto:wght@400&display=swap">
<style>
:root{
  --white:#ffffff;
  --brand-blue:#1569c7;
  --ink-grey:#4a4a4a;
  --footer-bg:#1c1c1c;
  --footer-rule:#3a3a3a;
  --hero-dark:#1a1008;
  --hero-mid:#7a4a1c;
  --hero-warm:#c98a45;
}
*{margin:0;padding:0;box-sizing:border-box}
html,body{width:1200px;height:729px;overflow:hidden;background:var(--footer-bg)}
body{position:relative;font-family:'Montserrat',sans-serif;color:var(--white)}
.hero{position:absolute;left:0;top:0;width:1200px;height:588px;
  background:
    radial-gradient(ellipse 420px 380px at 760px 330px, rgba(201,138,69,.55), transparent 70%),
    linear-gradient(90deg,var(--hero-dark) 0%,#3d2612 25%,var(--hero-mid) 50%,var(--hero-warm) 80%,#b87d3e 100%);}
.site-header{position:absolute;left:0;top:0;width:1200px;height:77px;border-bottom:1px solid rgba(255,255,255,.45)}
.brand-panel{position:absolute;left:0;top:0}
.brand{position:absolute;left:183px;top:22px;display:flex;align-items:center;gap:7px}
.brand-mark{width:28px;height:28px;background:var(--brand-blue)}
.brand-name{font-weight:700;font-size:16px;color:var(--brand-blue);letter-spacing:.5px;line-height:1}
.main-nav{position:absolute;top:29px;left:623px;display:flex;font-weight:600;font-size:12px;letter-spacing:.6px}
.main-nav a{color:var(--white);text-decoration:none;margin-right:21px}
.donate{position:absolute;left:921px;top:23px;width:106px;height:26px;background:var(--brand-blue);
  color:var(--white);font-weight:700;font-size:8.5px;letter-spacing:1px;display:flex;align-items:center;justify-content:center;text-decoration:none}
.hero-copy{position:absolute;left:178px;top:203px}
.hero-title{font-weight:800;font-size:40px;line-height:45px;letter-spacing:-.3px;width:560px}
.hero-lead{margin-top:16px;font-weight:400;font-size:18.5px;line-height:23px;width:480px}
.reg-number{display:inline-block;margin-top:21px;border:1px solid var(--white);padding:0 16px;height:41px;line-height:39px;
  font-weight:600;font-size:12.5px;letter-spacing:1px}
.site-footer{position:absolute;left:0;top:588px;width:1200px;height:141px;background:var(--footer-bg)}
.footer-nav{position:absolute;top:28px;left:0;width:1200px;text-align:center;font-family:'Roboto',sans-serif;font-size:11px}
.footer-nav a{color:var(--white);text-decoration:none}
.footer-nav .sep{margin:0 6px}
.social{position:absolute;top:58px;left:556px;display:flex;gap:3px}
.social span{width:27px;height:27px;border-radius:50%;background:var(--white)}
.footer-rule{position:absolute;left:173px;top:103px;width:854px;height:1px;background:var(--footer-rule)}
.copyright{position:absolute;top:115px;left:0;width:1200px;text-align:center;font-size:9.5px}
</style>
</head>
<body>
<div class="hero" role="img" aria-label="Photograph of a smiling child catching splashing water against a warm ochre wall"></div>

<header class="site-header">
  <svg class="brand-panel" width="420" height="77" viewBox="0 0 420 77"><polygon points="0,0 415,0 371,77 0,77" fill="#ffffff"/></svg>
  <div class="brand"><span class="brand-mark"></span><span class="brand-name">CORVELLA FOUNDATION</span></div>
  <nav class="main-nav"><a href="#">Home</a><a href="#">About us</a><a href="#">Grants</a><a href="#">Contact Us</a></nav>
  <a class="donate" href="#">MAKE DONATION</a>
</header>

<section class="hero-copy">
  <h1 class="hero-title">Corvella Foundation is a grant making charity set up in the UK in 2021</h1>
  <p class="hero-lead">The main aim of Corvella Foundation is to reduce the suffering caused by chronic pain.</p>
  <div class="reg-number">CHARITY REGISTRATION NUMBER 1187654</div>
</section>

<footer class="site-footer">
  <nav class="footer-nav"><a href="#">Home</a><span class="sep">&nbsp;&nbsp;|</span><a href="#">About</a><span class="sep">|</span><a href="#">Grants</a><span class="sep">|</span><a href="#">Contact</a><span class="sep">|</span><a href="#">Site Map</a></nav>
  <div class="social"><span></span><span></span><span></span></div>
  <div class="footer-rule"></div>
  <p class="copyright">© Corvella Foundation 2021. All Rights Reserved.</p>
</footer>
</body>
</html>
```